Housecleaning advertisement

We are a professional residential housecleaning service, in business since 2005, providing detailed, eco-friendly housecleaning to our clients. We are looking for a design that can be used in monthly coupon books ( 4c), quarterly local magazine (biz card sized 4c) and weekly newspaper ad (biz card sized b/w). We are looking for a retro feel - think 1940s kitchens - yellow, turquoise, bright red. we want to stress that we are a local firm, not a one-size fits all franchise. We provide very personalized service (linen changes, pet-friendly, flexible scheduling, sit down with customer prior to initial cleaning and discuss their priorities so that we know what they are looking for and deliver 110% each and every clean to them - and a a very reasonable price.) Our logo is a red car with two cleaners in it. Text for the ad :
Relax and enjoy your sparkling, clean, ready-for-company home!
Test drive our detailed, eco-friendly housecleaning
four hours for $100 (new clients only)
some bulleted points
* 100% Woman-owned and staffed. We know how to clean and tidy up - and treat your home with care and respect.
* Eco-friendly products - healthier for you and your family
* Fully insured and bonded.
415.382.9164
www.tidwrencasa.net
Target Market(s)
Professional women ages 30-65 in the New Haven County, Ct market
Industry/Entity Type
Residential
Requirements
Nice to have
- retro 1940s 1950s

```html
<!DOCTYPE html>
<html lang="en">
<head>
<meta charset="utf-8">
<title>Tidwren Casa Housecleaning – Ad</title>
<link rel="stylesheet" href="https://fonts.googleapis.com/css2?family=Sanchez&family=Roboto+Condensed:wght@400&family=Zilla+Slab:wght@500&display=swap">
<style>
  :root{
    --yellow:#e4d51c;
    --yellow-stripe:#d6c52e;
    --turquoise:#87d0c4;
    --red:#d7391d;
    --teal:#0f5866;
    --shadow:#4a4630;
    --ink:#111;
    --grey-bg:#d2d2d2;
    --grey-stripe:#c3c3c3;
    --grey-band:#bcbcbc;
    --grey-dark:#222;
    --grey-mid:#6a6a6a;
    --grey-shadow:#5a5a5a;
  }
  *{margin:0;padding:0;box-sizing:border-box}
  html,body{width:1046px;height:1200px;overflow:hidden;background:#fff}
  .sheet{width:1046px;height:1200px;display:flex;flex-direction:column}
  .ad{
    position:relative;width:1046px;height:600px;border:2px solid var(--ink);overflow:hidden;
    background:repeating-linear-gradient(90deg,var(--bg) 0 22px,var(--bg-stripe) 22px 44px);
    font-family:"Sanchez",serif;text-align:center;
  }
  .ad--color{--bg:var(--yellow);--bg-stripe:var(--yellow-stripe);--band:var(--turquoise);--band-shadow:var(--shadow);
    --name:var(--teal);--accent:var(--red);--main:var(--teal);--art:#d44a3a;--art2:#f0c08a}
  .ad--mono{--bg:var(--grey-bg);--bg-stripe:var(--grey-stripe);--band:var(--grey-band);--band-shadow:var(--grey-shadow);
    --name:var(--grey-dark);--accent:var(--grey-mid);--main:var(--grey-dark);--art:#7a7a7a;--art2:#b0b0b0}
  .banner{position:absolute;left:0;top:0;width:1046px;height:200px}
  .banner .band{fill:var(--band)}
  .banner .band-shadow{fill:var(--band-shadow)}
  .logo-art{
    position:absolute;left:18px;top:6px;width:250px;height:150px;border-radius:40px 60px 30px 30px;
    background:linear-gradient(160deg,var(--art2) 0%,var(--art) 55%,var(--art) 100%);
  }
  .sparkle{
    position:absolute;left:850px;top:6px;width:70px;height:70px;border-radius:50%;
    background:radial-gradient(circle,#fff 0 18%,rgba(255,255,255,.5) 35%,rgba(255,255,255,0) 70%);
  }
  .brand-name{
    position:absolute;left:210px;top:40px;width:760px;text-align:left;
    font-family:"Sanchez",serif;font-size:52px;line-height:1;color:var(--name);white-space:nowrap;
  }
  .contact{
    position:absolute;left:275px;top:108px;font-family:"Roboto Condensed",sans-serif;
    font-size:40px;color:var(--accent);white-space:nowrap;letter-spacing:-.5px
  }
  .contact .web{margin-left:14px;font-family:"Sanchez",serif;font-size:37px;letter-spacing:-1px}
  .copy{position:absolute;left:0;right:0;top:188px}
  .copy p{white-space:nowrap;line-height:1}
  .headline{font-size:43px;color:var(--accent);line-height:1.32!important}
  .offer{font-size:35px;color:var(--main);margin-top:10px}
  .price{font-size:34px;color:var(--accent);margin-top:13px}
  .price .note{color:var(--main)}
  .point{font-size:32px;color:var(--main);margin-top:13px}
  .point--narrow{font-family:"Zilla Slab",serif;font-size:32px;letter-spacing:-1.2px;transform:scaleX(.86);margin-top:12px}
  .point--accent{color:var(--accent);transform:scaleX(.9)}
  .point--final{transform:scaleX(.92)}
</style>
</head>
<body>
<main class="sheet">
  <section class="ad ad--color">
    <svg class="banner" viewBox="0 0 1046 200" aria-hidden="true">
      <polygon class="band-shadow" points="965,30 1035,30 1010,80 1030,180 25,185 30,168 990,160"/>
      <polygon class="band" points="40,10 1000,10 970,88 1000,160 40,160"/>
    </svg>
    <div class="logo-art" role="img" aria-label="Company logo illustration: red convertible car"></div>
    <div class="sparkle" role="img" aria-label="Sparkle accent"></div>
    <h1 class="brand-name">Tidwren Casa Housecleaning</h1>
    <p class="contact">Tel: 415.382.9164 <span class="web">www.tidwrencasa.net</span></p>
    <div class="copy">
      <p class="headline">Relax and enjoy your sparkling, clean,<br>ready-for-company home!</p>
      <p class="offer">Test drive our detailed, Eco-friendly housecleaning</p>
      <p class="price">four hours for $100 <span class="note">(new clients only)</span></p>
      <p class="point">100% Woman-owned and staffed</p>
      <p class="point point--narrow">We know how to clean and tidy up - and treat your home with care and respect</p>
      <p class="point point--accent">Eco-friendly products - healthier for you and your family</p>
      <p class="point point--final">Fully insured and bonded</p>
    </div>
  </section>
  <section class="ad ad--mono">
    <svg class="banner" viewBox="0 0 1046 200" aria-hidden="true">
      <polygon class="band-shadow" points="965,30 1035,30 1010,80 1030,180 25,185 30,168 990,160"/>
      <polygon class="band" points="40,10 1000,10 970,88 1000,160 40,160"/>
    </svg>
    <div class="logo-art" role="img" aria-label="Company logo illustration: convertible car, greyscale"></div>
    <div class="sparkle" role="img" aria-label="Sparkle accent"></div>
    <h2 class="brand-name">Tidwren Casa Housecleaning</h2>
    <p class="contact">Tel: 415.382.9164 <span class="web">www.tidwrencasa.net</span></p>
    <div class="copy">
      <p class="headline">Relax and enjoy your sparkling, clean,<br>ready-for-company home!</p>
      <p class="offer">Test drive our detailed, Eco-friendly housecleaning</p>
      <p class="price">four hours for $100 <span class="note">(new clients only)</span></p>
      <p class="point">100% Woman-owned and staffed</p>
      <p class="point point--narrow">We know how to clean and tidy up - and treat your home with care and respect</p>
      <p class="point point--accent">Eco-friendly products - healthier for you and your family</p>
      <p class="point point--final">Fully insured and bonded</p>
    </div>
  </section>
</main>
</body>
</html>
```